Flyer Design

I'm looking for a new flyer design to help promote our landscape company, and some of our main service for the up and coming season. We're trying to position ourselves as a leader in our market, so obviously quality is important to us.

Our current promotion is 25% off the first month with signup of annual service.

Phone Number: (555) 213-0948
Website: verdlanex.com
Our tagline: "Your hands are full... Let us help"

The call to action: direct them to our website for a detailed list of services and to receive a free quote.

You're welcome to add your own wording and punctuation. If I like the design I will provide feedback accordingly.

I have attached a jpg of our logo to help with design colors. I will provide the vector file upon completion of this project.

Also, I've attached a few photos that I had on hand of our companies work that may help with the design. Obviously I don't want to use them all, but there are a couple just to help out. I'm not opposed to stock photos either.
Thanks

Target Market(s)

We market to high end customers, generally with home between $500k-$2mil, or household income over $200k. Quality and creativity are most important to us.

Industry/Entity Type

Landscape

Requirements
Must have
• Creativity, easy to read, modern style.

```html
<!DOCTYPE html>
<html lang="en">
<head>
<meta charset="utf-8">
<title>Verdlane Door Hanger</title>
<link href="https://fonts.googleapis.com/css2?family=Montserrat:wght@600;700;800;900&family=Open+Sans:ital,wght@0,400;1,400;1,600&display=swap" rel="stylesheet">
<style>
  :root{
    --page:#e4e2de;
    --olive:#3e4330;
    --olive-dark:#2f3324;
    --orange:#e1601f;
    --ink:#2b2b2b;
    --grey:#555;
    --paper-top:#ffffff;
    --paper-bottom:#e7e7e7;
  }
  *{box-sizing:border-box;margin:0;padding:0}
  html,body{width:1200px;height:1000px;overflow:hidden;background:var(--page)}
  .hanger{
    position:absolute;left:420px;top:30px;width:360px;height:940px;
    background:linear-gradient(180deg,var(--paper-top),var(--paper-bottom));
    overflow:hidden;border-radius:3px;
    box-shadow:0 6px 18px rgba(0,0,0,.18);
    font-family:"Montserrat",sans-serif;
  }
  .hanger-top{
    position:absolute;left:0;top:0;width:100%;height:200px;
    background:linear-gradient(160deg,var(--olive),var(--olive-dark));
    clip-path:polygon(0 0,100% 0,100% 58%,0 100%);
  }
  .hanger-hole{
    position:absolute;left:52px;top:38px;width:124px;height:124px;border-radius:50%;
    background:var(--page);
  }
  .hanger-slit{
    position:absolute;left:104px;top:0;width:20px;height:42px;background:var(--page);
  }
  .photo{position:absolute;box-shadow:0 3px 8px rgba(0,0,0,.25);border:4px solid #fff}
  .photo-lawn{
    left:150px;top:112px;width:220px;height:190px;
    clip-path:polygon(22% 0,100% 0,100% 100%,0 100%);
    background:linear-gradient(180deg,#9fc0d8 0%,#b9a58a 35%,#4f7a34 55%,#5fa03a 100%);
  }
  .chevron{position:absolute;left:178px;top:190px;width:22px;height:28px}
  .laptop{
    position:absolute;left:20px;top:205px;width:132px;height:90px;
    background:linear-gradient(160deg,#d9d9d9,#8e8e8e);border-radius:4px;
  }
  .signup{position:absolute;left:22px;top:330px;color:var(--orange);font-weight:800}
  .signup-title{font-size:17px;letter-spacing:.5px}
  .signup-url{font-size:16px;font-weight:700;margin-top:2px}
  .services{
    position:absolute;left:14px;right:14px;top:392px;height:26px;
    border-top:1px solid #555;border-bottom:1px solid #555;
    display:flex;align-items:center;gap:6px;
    font-family:"Open Sans",sans-serif;font-size:9.5px;color:var(--ink);letter-spacing:.2px;
  }
  .services svg{flex:none}
  .headline{position:absolute;right:20px;top:428px;text-align:right;line-height:.95}
  .headline-earn{font-size:54px;font-weight:900;color:var(--ink);letter-spacing:1px}
  .headline-off{font-size:50px;font-weight:900;color:var(--orange)}
  .headline-today{font-size:42px;font-weight:900;color:var(--ink);letter-spacing:1px}
  .promo-rule{position:absolute;left:120px;right:20px;top:592px;border-top:1px solid #555}
  .promo-text{
    position:absolute;right:20px;top:600px;width:230px;text-align:right;
    font-family:"Open Sans",sans-serif;font-style:italic;font-size:12.5px;line-height:1.3;color:var(--grey);
  }
  .photo-house{
    left:-4px;top:660px;width:264px;height:190px;
    clip-path:polygon(0 0,88% 0,100% 100%,0 100%);
    background:linear-gradient(180deg,#c9dcec 0%,#c8b79c 30%,#a89884 55%,#4e8a34 72%,#5fa43e 100%);
  }
  .brand{position:absolute;right:14px;top:700px;width:96px;text-align:center}
  .brand-mark{width:58px;height:58px;border-radius:50%;background:var(--orange);margin:0 auto 8px}
  .brand-name{font-size:17px;font-weight:800;color:var(--ink);letter-spacing:.5px}
  .tagline{
    position:absolute;right:14px;top:810px;width:190px;text-align:right;
    font-family:"Open Sans",sans-serif;font-style:italic;font-weight:600;font-size:12.5px;color:var(--ink);
  }
  .hanger-bottom{
    position:absolute;left:0;bottom:0;width:100%;height:100px;
    background:linear-gradient(160deg,var(--olive),var(--olive-dark));
    clip-path:polygon(0 22%,100% 0,100% 100%,0 100%);
    color:#fff;padding:36px 0 0 26px;
  }
  .contact-phone{display:flex;align-items:center;gap:10px;font-size:22px;font-weight:800;letter-spacing:.5px}
  .phone-icon{width:26px;height:26px;border-radius:50%;background:var(--orange);display:flex;align-items:center;justify-content:center}
  .contact-web{font-size:18px;font-weight:800;margin-top:4px;letter-spacing:.3px}
</style>
</head>
<body>
  <div class="hanger">
    <div class="hanger-top"></div>
    <div class="hanger-hole"></div>
    <div class="hanger-slit"></div>

    <div class="photo photo-lawn" role="img" aria-label="Photo of a neatly mowed front lawn with shrubs beside a stucco home"></div>
    <svg class="chevron" viewBox="0 0 22 28"><polygon points="16,0 22,0 8,14 22,28 16,28 2,14" fill="var(--orange)"/></svg>

    <div class="laptop" role="img" aria-label="Laptop showing the company website"></div>

    <div class="signup">
      <div class="signup-title">SIGN UP NOW!</div>
      <div class="signup-url">www.verdlanex.com</div>
    </div>

    <div class="services">
      <svg width="14" height="16" viewBox="0 0 14 16"><polyline points="3,2 10,8 3,14" fill="none" stroke="var(--olive)" stroke-width="3"/></svg>
      <span>SNOW REMOVAL | MOWING | TREE MAINTENANCE | AERATION</span>
    </div>

    <div class="headline">
      <div class="headline-earn">EARN</div>
      <div class="headline-off">25% OFF</div>
      <div class="headline-today">TODAY</div>
    </div>

    <div class="promo-rule"></div>
    <p class="promo-text">Visit our site and sign up to recieve 25% off your first month of annual service.</p>

    <div class="photo photo-house" role="img" aria-label="Photo of a two-storey home with a manicured lawn and red-leaf tree"></div>

    <div class="brand">
      <div class="brand-mark"></div>
      <div class="brand-name">VERDLANE</div>
    </div>
    <p class="tagline">"Your hands are full... Let us help"</p>

    <div class="hanger-bottom">
      <div class="contact-phone">
        <span class="phone-icon">
          <svg width="14" height="14" viewBox="0 0 24 24"><path fill="#fff" d="M6.6 10.8a15 15 0 0 0 6.6 6.6l2.2-2.2a1 1 0 0 1 1-.25 11.4 11.4 0 0 0 3.6.57 1 1 0 0 1 1 1V20a1 1 0 0 1-1 1A17 17 0 0 1 3 4a1 1 0 0 1 1-1h3.5a1 1 0 0 1 1 1c0 1.25.2 2.45.57 3.57a1 1 0 0 1-.25 1z"/></svg>
        </span>
        <span>(555) 213-0948</span>
      </div>
      <div class="contact-web">www.verdlanex.com</div>
    </div>
  </div>
</body>
</html>
```